Storm Restoration Contractor needs a professional business card design

Looking for a professional business card design. Not looking for your cheapo MS Word standard ones that are readily available. Dont want it to be cookie cutter look like ones readily available online. We just recently changed our logo and want to freshen up all our documents. Our company handles restoring a property back to a pre-loss condition after a storm damages it. For example, wind, hail, flood, fire losses.

Target Market(s)

Property Owners, Homeowners, Property Owners, Commercial Property Owners, Property Management Companies, Hail and Wind Damaged Properties

Industry/Entity Type

Construction Company

Contact Information for Business Card

Brightline Facades
847-555-0193
847-555-0147 fax
www.brightlinefacades.example
info@brightlinefacades.example

Requirements
Must have
• Clean, Professional, fresh look
• Storm Restoration, Roofing, Siding, Windows
Nice to have
• If there is a way to incorporate storms that may be cool.

```html
<!DOCTYPE html>
<html lang="en">
<head>
<meta charset="utf-8">
<title>Brightline Facades — Business Card</title>
<link href="https://fonts.googleapis.com/css2?family=Open+Sans:wght@400;600;700&display=swap" rel="stylesheet">
<style>
  :root {
    --stage-top: #2a2a2a;
    --stage-bottom: #050505;
    --card-white: #ffffff;
    --brand-blue: #1b74bf;
    --brand-blue-text: #1a6fb8;
    --ink-grey: #4a4a4a;
    --brand-grey: #55575a;
  }
  * { margin: 0; padding: 0; box-sizing: border-box; }
  html, body { width: 1200px; height: 900px; overflow: hidden; }
  body {
    position: relative;
    background: linear-gradient(180deg, var(--stage-top) 0%, #1b1b1b 45%, var(--stage-bottom) 100%);
    font-family: "Open Sans", Arial, sans-serif;
  }
  .card {
    position: absolute;
    top: 306px;
    width: 440px;
    height: 271px;
    border-radius: 10px;
    box-shadow: 0 4px 10px rgba(0,0,0,0.45);
  }
  .card--front { left: 149px; background: var(--card-white); }
  .card--back { left: 608px; background: var(--brand-blue); }

  .front-brand {
    position: absolute;
    left: 50px; top: 48px;
    width: 150px; height: 136px;
    display: flex; align-items: center; justify-content: center;
    text-align: center;
    color: var(--brand-blue-text);
    font-weight: 700;
    font-size: 22px;
    line-height: 1.15;
  }

  .person { position: absolute; left: 231px; top: 52px; }
  .person__name { color: var(--brand-blue-text); font-weight: 600; font-size: 15px; line-height: 20px; }
  .person__title { color: var(--ink-grey); font-size: 12px; line-height: 16px; }

  .contacts { position: absolute; left: 231px; top: 108px; list-style: none; }
  .contacts li {
    display: flex; align-items: center;
    height: 16px;
    color: var(--ink-grey);
    font-size: 12px;
  }
  .contacts svg { width: 9px; height: 9px; margin-right: 7px; fill: var(--brand-blue-text); flex: none; }

  .services {
    position: absolute; left: 0; right: 0; top: 211px;
    text-align: center;
    color: var(--brand-blue-text);
    font-size: 13.5px;
  }

  .back-brand {
    position: absolute; left: 76px; top: 98px;
    display: flex; align-items: center;
  }
  .back-brand__dot {
    width: 74px; height: 74px; border-radius: 50%;
    background: var(--card-white);
    margin-right: 12px;
  }
  .back-brand__name {
    color: var(--card-white);
    font-weight: 700;
    font-size: 28px;
    line-height: 1.05;
    padding-left: 4px;
  }
</style>
</head>
<body>
  <section class="card card--front" aria-label="Business card front">
    <div class="front-brand">Brightline<br>Facades</div>

    <div class="person">
      <p class="person__name">Daniel Rourke</p>
      <p class="person__title">Managing Director</p>
    </div>

    <ul class="contacts">
      <li>
        <svg viewBox="0 0 10 10" aria-hidden="true"><path d="M2 0.5 3.6 2.4 2.8 3.5C3.4 4.9 5.1 6.6 6.5 7.2L7.6 6.4 9.5 8 8.6 9.5C4.5 9.3 0.7 5.5 0.5 1.4Z"/></svg>
        847-555-0193
      </li>
      <li>
        <svg viewBox="0 0 10 10" aria-hidden="true"><path d="M2 0h5v3H2zM0 3.5h10V9H0zM2 6h6v3.5H2z"/></svg>
        847-555-0147
      </li>
      <li>
        <svg viewBox="0 0 10 10" aria-hidden="true"><path d="M0 2h10v6H0zM0.5 2.3 5 5.5 9.5 2.3" stroke="#fff" stroke-width="0.8"/></svg>
        info@brightlinefacades.example
      </li>
      <li>
        <svg viewBox="0 0 10 10" aria-hidden="true"><circle cx="5" cy="5" r="4.8"/></svg>
        www.brightlinefacades.example
      </li>
    </ul>

    <p class="services">Storm Restoration | Roofing | Siding | Windows</p>
  </section>

  <section class="card card--back" aria-label="Business card back">
    <div class="back-brand">
      <span class="back-brand__dot" aria-hidden="true"></span>
      <span class="back-brand__name">Brightline<br>Facades</span>
    </div>
  </section>
</body>
</html>
```